Wix web design for healthcare IT consulting firm.

I am looking for a web design built in Wix that it will be easy for me to add or edit content in the future. The web site does not need to be overly complicated, but it should look very polished and professional. I also want to ensure it is mobile device friendly. I do not need any type of on-line purchasing ability. I will eventually do blogs, but for now it is a fairly standard web site with main page, about us, services provided, etc. I would also like a place for potential customers to contact us directly from the web site. I have included a Word document with some content for the web design. I have also included my logo and business card for reference. I would like to utilize similar colors as my business card. One of my primary competitors is https://vontalmhc.example/

Target Market(s)

Target market could be nursing home CEO, CIO, or other leader at an organization that manages long term care facilities.

Number of Pages Required

5+ page

Colors
876aae

Requirements
Must have
• Be designed to be used in Wix. Use the content I provided to create and make web design. Allow to be viewed on mobile device. Please use similar color structure as attached business card. Please use attached logo in design.

```html
<!DOCTYPE html>
<html lang="en">
<head>
<meta charset="utf-8">
<title>Brightwell Healthcare Solutions</title>
<link rel="stylesheet" href="https://fonts.googleapis.com/css2?family=Open+Sans:wght@300;400;600;700&display=swap">
<style>
:root{
  --purple:#876aae;
  --purple-deep:#7d58a8;
  --purple-form:#8460ab;
  --purple-bright:#9a68d8;
  --card-1:#a07fcf;
  --card-2:#9462d6;
  --card-3:#8a4fd3;
  --ink:#3a3a3a;
  --muted:#8a8a8a;
  --white:#ffffff;
  --footer:#e8e8eb;
  --footer-bar:#f1f1f3;
  --line:#e4e4e8;
}
*{box-sizing:border-box;margin:0;padding:0}
html,body{width:719px;height:1200px;overflow:hidden}
body{position:relative;background:var(--white);font-family:"Open Sans",Arial,sans-serif;color:var(--ink)}
.abs{position:absolute}

/* header */
.site-header{left:0;top:0;width:719px;height:44px;background:var(--white)}
.brand{left:124px;top:9px;height:28px;padding:0 6px;display:flex;align-items:center;gap:5px;color:var(--purple);font-weight:700;font-size:16px;letter-spacing:-.3px}
.brand-dot{width:8px;height:8px;border-radius:50%;background:var(--purple)}
.nav a{position:absolute;top:16px;font-size:8.5px;color:var(--ink);text-decoration:none}
.nav a.active{color:var(--purple);font-weight:600}
.nav .nav-cta{top:13px;width:63px;height:19px;background:var(--purple);color:var(--white);text-align:center;line-height:19px}

/* hero */
.hero{left:0;top:44px;width:719px;height:281px;background:linear-gradient(100deg,#dadadc 0%,#e4e4e6 55%,#ededef 100%)}
.hero-photo{right:0;top:0;width:330px;height:281px;background:radial-gradient(circle at 65% 55%,#f4f4f4 0%,#e2e3e5 45%,transparent 70%)}
.hero-title{left:123px;top:116px;font-size:22px;font-weight:600;color:var(--purple-bright);line-height:1.1}
.hero-sub{left:123px;top:138px;font-size:18px;font-weight:600;color:var(--white)}
.hero-text{left:123px;top:167px;width:262px;font-size:8.6px;line-height:11.4px;color:var(--white)}
.hero-btn{left:124px;top:247px;width:93px;height:32px;border:2px solid var(--purple);color:var(--purple-deep);font-size:10px;font-weight:600;text-align:center;line-height:28px}

/* section backgrounds */
.hex-bg{left:0;top:325px;width:719px;height:620px;background:radial-gradient(ellipse at 30% 40%,rgba(225,232,246,.45),transparent 60%),radial-gradient(ellipse at 80% 70%,rgba(225,232,246,.35),transparent 55%)}

.eyebrow{font-size:5.5px;font-weight:700;color:var(--purple);letter-spacing:.3px;text-transform:uppercase}
.section-title{font-size:13px;color:var(--ink)}

/* contact form */
.form-panel{left:124px;top:395px;width:263px;height:282px;background:var(--purple-form)}
.field{position:absolute;background:var(--white);font-size:7.5px;color:#555;padding:0 5px;line-height:20px}
.field.select{display:flex;justify-content:space-between;padding-right:0}
.select-arrow{width:22px;height:20px;background:#c9b6e2;display:flex;align-items:center;justify-content:center}
.field.message{line-height:14px;padding-top:3px}
.form-submit{position:absolute;left:156px;top:223px;width:90px;height:33px;background:var(--white);color:var(--purple-deep);font-size:8px;font-weight:600;text-align:center;line-height:33px}

/* contact details */
.intro{left:404px;top:392px;width:196px;font-size:8.2px;line-height:11px;color:var(--ink)}
.intro-body{left:404px;top:430px;width:196px;font-size:6.8px;line-height:9.6px;color:var(--muted)}
.detail{left:404px;width:196px;height:30px;display:flex;align-items:center;gap:9px;font-size:10.5px;color:var(--muted);border-bottom:1px solid var(--line)}
.detail b{font-weight:400;color:var(--ink)}
.social-label{left:408px;top:640px;font-size:10px;color:var(--muted)}
.social-dot{top:660px;width:16px;height:16px;border-radius:50%;background:var(--purple)}

/* cards */
.card{top:774px;width:157px;height:116px;padding:12px 10px;color:var(--white);box-shadow:0 3px 6px rgba(0,0,0,.14)}
.card h3{font-size:9.5px;font-weight:400;margin-bottom:6px}
.card p{font-size:5.6px;line-height:7.6px;opacity:.92}
.card .more{position:absolute;left:10px;bottom:10px;border:1px solid var(--white);font-size:5.6px;padding:2px 4px}
.card-1{left:124px;background:var(--card-1)}
.card-2{left:281px;background:var(--card-2)}
.card-3{left:438px;background:var(--card-3)}

/* mission */
.mission{left:0;top:945px;width:719px;height:126px;background:linear-gradient(180deg,#f6f8fd 0%,#e3ebfa 60%,#f0f4fc 100%)}
.mission-title{left:0;width:719px;top:985px;text-align:center;font-size:12px;font-weight:700;color:var(--purple)}
.mission-sub{left:0;width:719px;top:1001px;text-align:center;font-size:8px;color:var(--ink)}
.mission-btn{left:314px;top:1029px;width:93px;height:27px;background:var(--card-1);color:var(--white);font-size:8px;font-weight:600;text-align:center;line-height:27px}

/* footer */
.site-footer{left:0;top:1071px;width:719px;height:106px;background:var(--footer)}
.footer-brand{left:124px;top:1088px}
.footer-dot{top:1125px;width:8px;height:8px;border-radius:50%;background:#555}
.footer-head{top:1087px;font-size:8.5px;font-weight:700;color:var(--purple)}
.footer-list{top:1104px;list-style:none;font-size:5.8px;line-height:13px;color:#666}
.footer-contact{left:478px;top:1106px;font-size:6px;line-height:12px;color:#777}
.footer-contact b{color:var(--purple);font-weight:600}
.footer-bar{left:0;top:1177px;width:719px;height:23px;background:var(--footer-bar);border-top:1px solid #ddd;text-align:center;font-size:5.4px;line-height:22px;color:#666}
</style>
</head>
<body>

<header class="abs site-header">
  <div class="abs brand"><span class="brand-dot"></span>Brightwell</div>
  <nav class="nav">
    <a href="#" style="left:303px">Home</a>
    <a href="#" style="left:348px">About Us</a>
    <a href="#" style="left:405px">Services</a>
    <a href="#" class="active" style="left:459px">Contact Us</a>
    <a href="#" class="nav-cta" style="left:533px">Get Started</a>
  </nav>
</header>

<section class="abs hero">
  <div class="abs hero-photo" role="img" aria-label="Photo of an open medicine bottle with scattered teal and dark green capsules on a light grey surface"></div>
</section>
<h1 class="abs hero-title">Increasing the value and security</h1>
<h2 class="abs hero-sub">of your technology resources</h2>
<p class="abs hero-text">We understand different organizations have different needs. Brightwell HCS strives to assist your organization by bringing solutions that are easy to understand and allow the customer to track success. We provide solutions based on the customer's needs and desires.</p>
<div class="abs hero-btn">Get Started</div>

<div class="abs hex-bg" role="img" aria-label="Faint hexagon network pattern in pale blue"></div>

<div class="abs eyebrow" style="left:124px;top:355px">Contact Us</div>
<h2 class="abs section-title" style="left:124px;top:362px">Let's get to work right now</h2>

<form class="abs form-panel">
  <div class="field" style="left:19px;top:24px;width:107px">First Name</div>
  <div class="field" style="left:140px;top:24px;width:107px">Last Name</div>
  <div class="field" style="left:19px;top:60px;width:107px">Email</div>
  <div class="field" style="left:140px;top:60px;width:107px">Phone Number</div>
  <div class="field select" style="left:19px;top:100px;width:228px">What are you interested in?
    <span class="select-arrow"><svg width="8" height="5" viewBox="0 0 8 5"><path d="M0 0 L4 5 L8 0Z" fill="#fff"/></svg></span>
  </div>
  <div class="field message" style="left:19px;top:135px;width:228px;height:73px">Your message</div>
  <div class="form-submit">Contact Us</div>
</form>

<p class="abs intro">Are you ready to maximize excellent care AND cash flow with total revenue cycle management?</p>
<p class="abs intro-body">Our team works alongside your leadership to review systems, reduce risk and improve daily workflows. We study how each facility operates, listen to staff, and design a clear plan that fits your goals and budget. From assessment to rollout, we stay close to measure progress, train your people and keep every record secure and available when care teams need it most. Our approach is practical, honest and built around long term care.</p>

<div class="abs detail" style="top:573px">
  <svg width="11" height="11" viewBox="0 0 24 24"><path d="M6.6 10.8a15.1 15.1 0 0 0 6.6 6.6l2.2-2.2c.3-.3.7-.4 1-.2 1.1.4 2.3.6 3.6.6.6 0 1 .4 1 1V20c0 .6-.4 1-1 1C10.6 21 3 13.4 3 4c0-.6.4-1 1-1h3.5c.6 0 1 .4 1 1 0 1.3.2 2.5.6 3.6.1.3 0 .7-.2 1z" fill="var(--purple)"/></svg>
  <span>Call us: <b>555-014-2290</b></span>
</div>
<div class="abs detail" style="top:605px">
  <svg width="11" height="9" viewBox="0 0 22 16"><rect x="0" y="0" width="22" height="16" fill="var(--purple)"/><path d="M0 0 L11 8 L22 0" stroke="#fff" stroke-width="1.5" fill="none"/></svg>
  <span>Email us: <b>555-014-2290</b></span>
</div>
<div class="abs social-label">Social Networks:</div>
<span class="abs social-dot" style="left:411px"></span>
<span class="abs social-dot" style="left:448px"></span>
<span class="abs social-dot" style="left:485px"></span>

<div class="abs eyebrow" style="left:124px;top:718px">Site Materials</div>
<h2 class="abs section-title" style="left:124px;top:725px">Additional information you may like to know</h2>

<article class="abs card card-1">
  <h3>Our Services</h3>
  <p>We assess, plan and support the systems that keep your facilities running smoothly, safely and in line with current rules.</p>
  <span class="more">Read More</span>
</article>
<article class="abs card card-2">
  <h3>Our Team</h3>
  <p>Meet the consultants who bring years of healthcare IT experience to every project, large or small, across the region.</p>
  <span class="more">Read More</span>
</article>
<article class="abs card card-3">
  <h3>Contact Us</h3>
  <p>Reach out with a question or a project idea and our team will reply within one business day.</p>
  <span class="more">Read More</span>
</article>

<section class="abs mission" role="img" aria-label="Band with a soft blue hexagon pattern"></section>
<h2 class="abs mission-title">OUR MISSION IS TO PARTNER WITH CUSTOMERS</h2>
<p class="abs mission-sub">To increase the value of their technology tools</p>
<div class="abs mission-btn">Contact Us</div>

<footer class="abs site-footer"></footer>
<div class="abs brand footer-brand"><span class="brand-dot"></span>Brightwell</div>
<span class="abs footer-dot" style="left:143px"></span>
<span class="abs footer-dot" style="left:159px"></span>
<span class="abs footer-dot" style="left:175px"></span>

<h3 class="abs footer-head" style="left:262px">Our Services</h3>
<ul class="abs footer-list" style="left:262px">
  <li>Risk Assessment</li>
  <li>Policy Management</li>
  <li>Chief Information Officer</li>
  <li>Chief Information Security Officer</li>
  <li>IT Department Evaluation</li>
</ul>
<ul class="abs footer-list" style="left:379px">
  <li>EHR Optimization Services</li>
  <li>EHR Implementation</li>
  <li>EHR Assessment</li>
  <li>EHR Quality Assessment</li>
  <li>EHR Quality Assessment</li>
</ul>
<h3 class="abs footer-head" style="left:478px">Contact Us</h3>
<p class="abs footer-contact">Email us: <b>mlane@brightwellhcs.example</b><br>Call us: <b>555-014-2290</b></p>

<div class="abs footer-bar">©Brightwell HealthCare. All Rights Reserved.</div>

</body>
</html>
```